Webdesign für Herstellung von Geschenk- und Dekorationsartikeln
Kobalt Prismo ist ein sehr angenehmer und professioneller Designer, der sich viele Gedanken über mein Projekt gemacht hat und ein Design, passend zu meinen Artikeln entworfen hat. Neben einer kompetenten Beratung gab es viele hilfreiche Vorschläge, die über den eigentlichen Auftrag hinaus gingen. Der Designer ist sehr zu empfehlen. Vielen Dank für den freundlichen Kontakt!
Zielgruppe
Wir sind eine kleine Firma, die mit einem Lasergravierer Geschenk- und Dekorationsartikel herstellt, verziert und beschriftet. Hierzu wird hauptsächlich Holz, Papier, Kork, Filz und Glas als Material eingesetzt.
Auch Schmuck , wie z.B. Kettenanhänger und Ohrringe aus Holz werden gefertigt.
Außerdem werden Fotogravur-Arbeiten nach Kundenwunsch angeboten.
Haupt-Zielgruppe sind Frauen ab 30.
Aufgabenstellung
Das Design soll etwas verspielt sein und Freude an den kleinen Dingen des Lebens ausdrücken. Es soll nicht zu sachlich und kühl sein.
Das vorhandene Logo wird bereit gestellt.
Es existiert noch keine Webseite. Die zukünftige Webseite soll über einen Shop verfügen.
Von der Shop-Darstellung her, hat mir die Webseite 'www.qvhauswerk.ch' gefallen.
Es wäre gut, wenn die im Logo vorhandenen Farben auch auf dem Design für die Webseite auftauchen würden.
Als Design-Tool wäre Adobe Photoshop (PSD) für die Erstellung gut.

```html
<!DOCTYPE html>
<html lang="de">
<head>
<meta charset="utf-8">
<title>Brennholm Laserdeko</title>
<link href="https://fonts.googleapis.com/css2?family=Open+Sans:ital,wght@0,400;0,600;0,700;1,700&family=Dancing+Script:wght@600&display=swap" rel="stylesheet">
<style>
:root{
  --cork:#b57a3f;
  --cork-dark:#a56a32;
  --brown:#7a4421;
  --gold:#b8823f;
  --text:#2b2b2b;
  --price:#3d9a27;
  --line:#d9d4d0;
  --white:#ffffff;
}
*{margin:0;padding:0;box-sizing:border-box}
html,body{width:1100px;height:1200px;overflow:hidden;background:var(--white)}
body{position:relative;font-family:"Open Sans",sans-serif;color:var(--text)}
.abs{position:absolute}
.backdrop{position:absolute;left:0;top:0}
.topbar{font-size:5.5px;top:8px;color:var(--text)}
.nav{top:32px;left:428px;display:flex;gap:13px;font-size:8px}
.nav .active{color:var(--gold);font-style:italic;font-weight:700}
.brand-mark{left:214px;top:14px;font-size:22px;font-weight:600;color:#5a4538}
.brand-mark small{display:block;font-size:5px;letter-spacing:1.5px;color:var(--gold);text-align:center;margin-top:-3px}
.hero-name{left:0;width:1100px;top:170px;text-align:center;font-size:78px;font-weight:600;color:#8f5a2a;letter-spacing:2px}
.hero-sub{left:0;width:1100px;top:262px;text-align:center;font-size:18px;letter-spacing:6px;color:#6b4220}
.script{font-family:"Dancing Script",cursive;color:var(--brown);text-align:center;left:0;width:1100px;font-size:27px}
.copy{left:330px;width:440px;text-align:center;font-size:8.6px;line-height:13.8px}
.crumbs{left:776px;top:430px;font-size:7.5px;color:var(--gold)}
.cat-title{width:158px;text-align:center;font-size:13px;font-weight:600;color:var(--brown);top:444px}
.card{top:465px;width:158px;height:218px;border:1px solid var(--line);text-align:center;font-size:7.2px;line-height:11.5px}
.card .photo{height:166px;background:linear-gradient(#f7f6f5,#efeceb)}
.card .info{padding-top:4px}
.card .price{color:var(--price);font-weight:700}
.card .more{color:var(--gold);font-style:italic;font-weight:700}
.card .tools{position:absolute;right:8px;top:118px;display:flex;flex-direction:column;gap:5px}
.arrow{top:538px}
.video{left:385px;top:800px;width:326px;height:189px;background:radial-gradient(circle at 70% 30%,#c0504a 0 14%,transparent 30%),linear-gradient(135deg,#8c7f78,#b9aca2 55%,#8f8078)}
.video .bar{position:absolute;left:0;bottom:0;width:100%;height:10px;background:#151515}
.video .play{position:absolute;left:134px;top:67px;width:56px;height:39px;border-radius:10px;background:var(--white)}
.foot{color:var(--white);font-size:7.4px;line-height:12px;top:1110px}
.foot .caps{letter-spacing:2px;font-weight:700}
.foot-brand{left:490px;top:1092px;color:var(--white);font-size:22px;font-weight:600}
.pay{left:770px;top:1088px;display:flex;flex-direction:column;gap:8px}
.pay span{display:block;width:28px;height:10px;border-radius:3px;background:rgba(255,255,255,.85)}
</style>
</head>
<body>
<svg class="backdrop" width="1100" height="1200" role="img" aria-label="Korkstruktur als Hintergrund von Kopfbereich und Fußzeile">
  <defs><linearGradient id="cork" x1="0" y1="0" x2="1" y2="1"><stop offset="0" stop-color="#bb8145"/><stop offset="1" stop-color="#a9713a"/></linearGradient></defs>
  <path d="M0,35 Q550,85 1100,35 L1100,330 Q550,280 0,330 Z" fill="url(#cork)"/>
  <path d="M0,1058 Q550,1105 1100,1058 L1100,1200 L0,1200 Z" fill="url(#cork)"/>
</svg>

<div class="abs brand-mark">Brennholm<small>LASERDEKO</small></div>
<div class="abs topbar" style="left:603px">+49 (0) 351 20 48 16</div>
<div class="abs topbar" style="left:679px">Login &nbsp;| &nbsp;Registrieren</div>
<svg class="abs" style="left:762px;top:3px" width="125" height="16" fill="none" stroke="#333" stroke-width="1">
  <circle cx="8" cy="5" r="3.5"/><path d="M2,14 Q8,7 14,14 Z"/>
  <path d="M55,7 H69 L67,13 H57 Z M58,7 L62,3 L66,7"/>
  <path d="M115,14 L109,8 A3,3 0 0 1 115,5 A3,3 0 0 1 121,8 Z"/>
</svg>
<nav class="abs nav"><span>Home</span><span>Holzschmuck</span><span class="active">Wanddeko</span><span>Wunschgravuren</span><span>Alltagsdinge</span><span>Weihnachten</span><span>Ostern</span><span>Kontakt</span></nav>
<svg class="abs" style="left:845px;top:31px" width="40" height="10" fill="#222"><rect x="0" y="1" width="7" height="8"/><rect x="13" y="1" width="8" height="8" rx="2"/><rect x="27" y="1" width="11" height="8" rx="2"/></svg>

<div class="abs hero-name">Brennholm</div>
<div class="abs hero-sub">LASERDEKO</div>

<h1 class="abs script" style="top:312px">Wir sind eine kleine Firma im ...</h1>
<p class="abs copy" style="top:352px">... Sächsischen die mit Lasergravierern Geschenk- und Dekorationsartikel herstellt, verziert und beschriftet. Hierzu wird hauptsächlich Holz, Papier, Kork, Filz und Glas als Material eingesetzt. Besonders Schmuck aus verschiedenen Holzarten, wie z.B. Kettenanhänger und Ohrringe fertigen wir, natürlich auch individuell nach Ihren Ideen - spezialisiert sind wir u.a. auch auf Foto- oder Glasgravuren.<br>Stöbern Sie in unserem Shop oder schicken Sie uns einfach eine <b><i>Nachricht</i></b> mit Ihrer Wunschgravur.</p>

<div class="abs crumbs">Alltagsdinge / Ostern / Sale →</div>

<svg class="abs arrow" style="left:194px" width="12" height="24" fill="none" stroke="#999" stroke-width="1.5"><path d="M10,2 L2,12 L10,22"/></svg>
<svg class="abs arrow" style="left:892px" width="12" height="24" fill="none" stroke="#999" stroke-width="1.5"><path d="M2,2 L10,12 L2,22"/></svg>

<div class="abs cat-title" style="left:214px">Holzschmuck</div>
<div class="abs cat-title" style="left:385px">Weihnachten</div>
<div class="abs cat-title" style="left:556px">Wanddeko</div>
<div class="abs cat-title" style="left:727px">Wunschgravuren</div>

<div class="abs card" style="left:214px">
  <div class="photo" role="img" aria-label="Ohrhänger in Engelflügelform aus Birkenholz"></div>
  <div class="info">z.B. Ohrhänger "Engelflügel"<br>aus Birkenholz<br>ab <span class="price">10,- €</span><br><span class="more">mehr Holzschmuck &gt;</span></div>
  <div class="tools"><svg width="12" height="40" fill="none" stroke="#6b4a2e" stroke-width="1"><ellipse cx="6" cy="4" rx="5" ry="3"/><circle cx="6" cy="4" r="1.2"/><path d="M1,16 H11 L10,21 H2 Z M3,16 L6,13 L9,16"/><path d="M6,38 L1.5,33 A2.5,2.5 0 0 1 6,30.5 A2.5,2.5 0 0 1 10.5,33 Z"/></svg></div>
</div>
<div class="abs card" style="left:385px">
  <div class="photo" role="img" aria-label="Tannenbaum aus erzgebirgischem Tannenholz"></div>
  <div class="info">Tannenbaum<br>aus erzgebirgischem Tannenholz<br>ab <span class="price">11,- €</span><br><span class="more">mehr Weihnachstartikel &gt;</span></div>
  <div class="tools"><svg width="12" height="40" fill="none" stroke="#6b4a2e" stroke-width="1"><ellipse cx="6" cy="4" rx="5" ry="3"/><circle cx="6" cy="4" r="1.2"/><path d="M1,16 H11 L10,21 H2 Z M3,16 L6,13 L9,16"/><path d="M6,38 L1.5,33 A2.5,2.5 0 0 1 6,30.5 A2.5,2.5 0 0 1 10.5,33 Z"/></svg></div>
</div>
<div class="abs card" style="left:556px">
  <div class="photo" role="img" aria-label="Wandbild mit Spruch auf dunkler Tafel"></div>
  <div class="info">z.B. Wandbilder<br>mit diversen Sprüchen<br>ab <span class="price">11,- €</span><br><span class="more">mehr Wanddeko &gt;</span></div>
  <div class="tools"><svg width="12" height="40" fill="none" stroke="#6b4a2e" stroke-width="1"><ellipse cx="6" cy="4" rx="5" ry="3"/><circle cx="6" cy="4" r="1.2"/><path d="M1,16 H11 L10,21 H2 Z M3,16 L6,13 L9,16"/><path d="M6,38 L1.5,33 A2.5,2.5 0 0 1 6,30.5 A2.5,2.5 0 0 1 10.5,33 Z"/></svg></div>
</div>
<div class="abs card" style="left:727px">
  <div class="photo" role="img" aria-label="Graviertes Whisky-Becherglas mit Namen und Datum"></div>
  <div class="info">z.B. Whisky-Becherglas<br>mit Namen / Geburtsdatum<br><br><span class="more">mehr Thema Wunschgravuren &gt;</span></div>
  <div class="tools"><svg width="12" height="40" fill="none" stroke="#6b4a2e" stroke-width="1"><ellipse cx="6" cy="4" rx="5" ry="3"/><circle cx="6" cy="4" r="1.2"/><path d="M1,16 H11 L10,21 H2 Z M3,16 L6,13 L9,16"/><path d="M6,38 L1.5,33 A2.5,2.5 0 0 1 6,30.5 A2.5,2.5 0 0 1 10.5,33 Z"/></svg></div>
</div>

<h2 class="abs script" style="top:698px">Lasergravur ... wie geht das eigentlich?</h2>
<p class="abs copy" style="top:738px;left:325px;width:450px">Bei der Lasergravur handelt es sich um ein Verfahren der Oberflächenbearbeitung, bei dem ein hochenergetischer Laserstrahl zur Beschriftung, Markierung oder Dekoration von Objekten genutzt wird. Das Material wird durch den auftreffenden Laserstrahl sehr stark erhitzt, das Material verdampft.Eine Lasergravur ist permanent, sehr abriebbeständig und langlebig.</p>

<div class="abs video" role="img" aria-label="Video: Laserkopf graviert ein Motiv auf Holz">
  <div class="play"><svg width="56" height="39"><path d="M21,11 L38,19.5 L21,28 Z" fill="#333"/></svg></div>
  <div class="bar"></div>
</div>

<h2 class="abs script" style="top:1002px;font-size:28px">Sie haben Fragen oder besondere Wünsche ...</h2>
<p class="abs copy" style="top:1040px;left:300px;width:500px;font-size:9px">Rufen Sie uns unverbindlich an: <i>0351 20 48 16</i> oder einfach mailen <i>info@brennholm.de</i></p>

<div class="abs foot-brand">Brennholm</div>
<div class="abs foot" style="left:303px">Home<br><span class="caps">MEIN KONTO</span><br>Kategorieübersicht<br>Versandkosten<br>FAQ Lasergravuren<br>
  <svg width="40" height="10" fill="#fff"><rect x="0" y="1" width="6" height="8"/><rect x="13" y="1" width="8" height="8" rx="2"/><rect x="27" y="1" width="11" height="8" rx="2"/></svg></div>
<div class="abs foot" style="left:458px">Kontakt<br>AGB<br>Impressum<br>Datenschutzerklärung<br>CookiePolicy<br>Copyright</div>
<div class="abs foot" style="left:626px">BRENNHOLM e.K.<br>Inhaberin Greta Lindner<br>Spanweg 4 - 01234 Dresden<br>Tel.: +49 (0) 351 20 48 16<br>Fax + 49 (0) 351 20 48 17<br>info@brennholm.de</div>
<div class="abs pay"><span></span><span style="height:18px"></span><span></span><span></span><span style="height:14px"></span><span></span></div>
</body>
</html>
```